Monthly Mailed Newsletter/Magazine for Medical Spa

Every month we send out a mailed newsletter/magazine to our visitors from the previous month. We made a sample newsletter/magazine as a guideline of what we are looking for. We need a designer to make a simple and clean design layout.

- Attached is our sample design that has all the content we want to use.
- Newsletter/magazine is 8 pages total.
- Size of each page is 8.5 inches in width by 11 inches in height.
- Content and images can be located here: https://files.vornacloud.net/shared/8kqTRw3ZpLmX2vNcA7yHd5EbJ0sUgFo4e?view=open

The following will give you an idea of our brand presentation.
Our website is: www.GlowDermaClinic.com
Our Instagram; @glowdermaclinic
Our Facebook: www.socialtreo.com/glowdermaclinic

Target Market(s)

Women 25 - 45

Industry/Entity Type

Beauty

Font styles to use
Other font styles liked:
• Josefins Sans Bold & Lato

Colors
f78f20
ffffff

Requirements
Must have
• - Our Logo
- Our tagline: YOUR SKIN DESERVES IT!
- Address and contact information for our locations
- Our color scheme: Black and #FAA641
- Heading font is Josefin Sans Bold
- Paragraph font is Lato
- Our website address: www.GlowDermaClinic.com

```html
<!DOCTYPE html>
<html lang="en">
<head>
<meta charset="utf-8">
<title>Glow Skin &amp; Laser Newsletter – November 2020</title>
<link rel="stylesheet" href="https://fonts.googleapis.com/css2?family=Anton&family=Josefin+Sans:wght@400;700&family=Lato:wght@400;700&display=swap">
<style>
  :root {
    --orange: #f9a03f;
    --orange-deep: #f78f20;
    --ink: #1b1b1b;
    --white: #ffffff;
    --board: #ffffff;
    --shadow: 3px 4px 6px rgba(0,0,0,.45);
  }
  * { box-sizing: border-box; margin: 0; padding: 0; }
  html, body { width: 1200px; height: 848px; overflow: hidden; }
  body { background: var(--board); font-family: "Lato", sans-serif; color: var(--ink); position: relative; }

  .abs { position: absolute; }
  .photo { position: absolute; }

  .board-label { position: absolute; font-family: "Lato", sans-serif; font-size: 27px; letter-spacing: 1px; color: var(--ink); transform: translateX(-50%); white-space: nowrap; }

  /* ---------- Cover ---------- */
  .cover { position: absolute; left: 108px; top: 190px; width: 364px; height: 471px; overflow: hidden; box-shadow: var(--shadow); }
  .cover-photo { inset: 0; background: linear-gradient(135deg, #c0a687 0%, #b89f82 40%, #cdb59b 70%, #e1d3c2 100%); }
  .masthead { left: 14px; top: 2px; font-family: "Anton", sans-serif; font-size: 94px; line-height: 1; color: var(--white); letter-spacing: 5px; }
  .masthead-bar { left: 14px; top: 88px; width: 203px; height: 9px; background: var(--orange); color: var(--white); font-size: 7.4px; letter-spacing: .4px; display: flex; justify-content: space-between; align-items: center; padding: 0 7px 0 2px; }
  .name-box { left: 256px; top: 15px; width: 93px; height: 92px; background: var(--white); display: flex; align-items: center; justify-content: center; }
  .name-box-text { font-family: "Josefin Sans", sans-serif; font-weight: 700; font-size: 26px; color: var(--ink); line-height: 1; }
  .cover-story { left: 14px; width: 230px; }
  .cover-story h2 { font-family: "Josefin Sans", sans-serif; font-weight: 700; font-size: 14.5px; line-height: 17px; letter-spacing: .5px; color: var(--ink); }
  .cover-story p { font-size: 8px; line-height: 10px; margin-top: 2px; color: var(--ink); width: 125px; }
  .cover-rule { left: 14px; width: 120px; height: 2px; background: var(--orange); }
  .thanks { left: 14px; top: 373px; font-family: "Josefin Sans", sans-serif; font-weight: 700; color: var(--white); text-shadow: 2px 2px 3px rgba(0,0,0,.55); line-height: 1; }
  .thanks .big { display: block; font-size: 37px; }
  .thanks .small { display: block; font-size: 27px; margin-top: 4px; }

  /* ---------- Spreads ---------- */
  .spread { position: absolute; left: 528px; width: 559px; height: 361px; background: var(--white); overflow: hidden; box-shadow: var(--shadow); }
  .spread-contents { top: 21px; }
  .spread-feature { top: 435px; }

  .thumb-num { position: absolute; right: 6px; font-family: "Josefin Sans", sans-serif; font-weight: 700; font-size: 36px; color: rgba(255,255,255,.8); text-shadow: 1px 1px 2px rgba(0,0,0,.35); line-height: 1; }

  .header-band { left: 123px; top: 13px; width: 436px; height: 42px; background: var(--orange); }
  .header-band span { position: absolute; top: 13px; font-family: "Josefin Sans", sans-serif; font-weight: 700; font-size: 17px; letter-spacing: .4px; color: var(--white); text-shadow: 1px 1px 2px rgba(0,0,0,.4); white-space: nowrap; }
  .band-contents { left: 16px; }
  .band-promos { right: 10px; }

  .promo-intro { left: 315px; top: 58px; width: 220px; font-size: 6.9px; line-height: 9px; font-weight: 700; }

  .toc-item { position: absolute; left: 140px; width: 140px; }
  .toc-num { position: absolute; left: 0; top: 1px; font-family: "Josefin Sans", sans-serif; font-weight: 700; font-size: 11px; }
  .toc-title { margin-left: 24px; font-size: 8.6px; line-height: 10.4px; color: var(--orange); text-transform: uppercase; }
  .toc-desc { margin-left: 24px; font-size: 6px; line-height: 8.6px; margin-top: 1px; }

  .promo { position: absolute; left: 293px; width: 150px; }
  .promo-dot { position: absolute; left: 0; top: 1px; width: 9px; height: 9px; border-radius: 50%; background: var(--orange); }
  .promo h3 { margin-left: 18px; font-size: 8.6px; font-weight: 400; color: var(--orange); line-height: 10px; white-space: nowrap; }
  .promo ul { list-style: none; margin-left: 18px; font-size: 6px; line-height: 9px; white-space: nowrap; }

  .feature-title { left: 17px; top: 44px; font-family: "Josefin Sans", sans-serif; font-weight: 700; color: var(--orange); line-height: 1; text-shadow: 1px 1px 2px rgba(0,0,0,.3); }
  .feature-title span { display: block; }
  .ft-is { font-size: 25px; }
  .ft-mid { font-size: 27px; margin-top: 8px; letter-spacing: .5px; }
  .ft-mid + .ft-mid { margin-top: 6px; }
  .ft-last { font-size: 37px; margin-top: 10px; letter-spacing: 1px; }

  .col { position: absolute; width: 127px; }
  .col h4 { font-size: 8.6px; line-height: 10.4px; font-weight: 400; color: var(--orange); }
  .col p { font-size: 4.65px; line-height: 5.9px; margin-top: 4px; }
  .col h4.next { margin-top: 7px; }
  .dropcap-rule { border-left: 1px solid var(--orange); padding-left: 2px; }
</style>
</head>
<body>

  <!-- Front cover -->
  <section class="cover">
    <div class="photo cover-photo" role="img" aria-label="Smiling client with dark hair wearing laser safety glasses, lying on a treatment bed"></div>
    <div class="abs masthead">GLOW</div>
    <div class="abs masthead-bar"><span>Skin &amp; Laser Newsletter</span><span>NOV 2020 issue 1</span></div>
    <div class="abs name-box"><span class="name-box-text">Glow</span></div>

    <div class="abs cover-story" style="top:111px">
      <h2>STAFF MEMBER<br>SPOTLIGHT</h2>
      <p style="width:130px">See every shade of burnt sienna along the hills of sand.</p>
    </div>
    <div class="abs cover-rule" style="top:174px"></div>
    <div class="abs cover-story" style="top:184px">
      <h2>IS AT-HOME<br>LASER HAIR<br>REMOVAL<br>EFFECTIVE?</h2>
      <p style="width:130px">Our team has provided you with the top ten must-haves.</p>
    </div>
    <div class="abs cover-rule" style="top:281px"></div>
    <div class="abs cover-story" style="top:289px">
      <h2>CAN YOU MAKE<br>YOUR TOX<br>LAST LONGER?</h2>
      <p style="width:125px">Places you need to see with your bare eyes. Buy your plane ticket now!</p>
    </div>
    <div class="abs thanks"><span class="big">Thank you</span><span class="small">for visiting us!</span></div>
  </section>
  <div class="board-label" style="left:297px; top:676px;">Front cover</div>

  <!-- Pages 1 & 2 -->
  <section class="spread spread-contents">
    <div class="photo" style="left:0;top:0;width:123px;height:93px;background:linear-gradient(135deg,#3a3550 0%,#c9a25a 45%,#e7b88f 100%)" role="img" aria-label="Gloved hand holding a laser device against skin"><span class="thumb-num" style="top:24px">02</span></div>
    <div class="photo" style="left:0;top:99px;width:123px;height:80px;background:linear-gradient(135deg,#e9e6e3 0%,#e4c8b2 55%,#f3f1ef 100%)" role="img" aria-label="At-home laser device on a leg"><span class="thumb-num" style="top:22px">03</span></div>
    <div class="photo" style="left:0;top:183px;width:123px;height:80px;background:linear-gradient(135deg,#e8c6aa 0%,#c8987b 50%,#3a2c28 100%)" role="img" aria-label="Injection treatment near the eye"><span class="thumb-num" style="top:10px;left:6px;right:auto">05</span></div>
    <div class="photo" style="left:0;top:269px;width:123px;height:80px;background:linear-gradient(135deg,#f3ede6 0%,#cbb3a0 45%,#2b2320 100%)" role="img" aria-label="Client looking into a hand mirror"><span class="thumb-num" style="top:10px">07</span></div>

    <div class="abs header-band">
      <span class="band-contents">CONTENTS</span>
      <span class="band-promos">NOVEMBER PROMOTIONS</span>
    </div>

    <p class="abs promo-intro">The following promotions are available to our active members. An annual payment of 59.99 gives you access to reduced pricing, member only packages, payment plans, and rewards.</p>

    <div class="toc-item" style="top:95px"><span class="toc-num">02</span><div class="toc-title">November 2020<br>Promotions</div><div class="toc-desc">Don't miss out on end of the year promotions.</div></div>
    <div class="toc-item" style="top:162px"><span class="toc-num">03</span><div class="toc-title">Is at-home laser hair<br>removal effective?</div><div class="toc-desc">Here are some unbiased professional opinions to zap away your FAQs.</div></div>
    <div class="toc-item" style="top:228px"><span class="toc-num">05</span><div class="toc-title">Can you make your<br>tox last longer?</div><div class="toc-desc">We sought advice from professionals to bring you the answer.</div></div>
    <div class="toc-item" style="top:293px"><span class="toc-num">07</span><div class="toc-title">Preview of next<br>weeks issue</div><div class="toc-desc">Take a peak at what's coming next!</div></div>

    <div class="promo" style="top:93px"><span class="promo-dot"></span><h3>LASER HAIR REMOVAL</h3><ul><li>1 Area&nbsp;&nbsp; - 6 pack - $294</li><li>2 Areas - 6 pack - $510</li><li>3 Areas - 6 pack - $726</li></ul></div>
    <div class="promo" style="top:133px"><span class="promo-dot"></span><h3>IPL: PHOTOFACIAL</h3><ul><li>1 Session&nbsp; - $89</li><li>2 Sessions - $178</li></ul></div>
    <div class="promo" style="top:164px"><span class="promo-dot"></span><h3>MICRONEEDLING</h3><ul><li>1 Treatment&nbsp; - $150</li><li>2 Treatments - $290</li><li>With PRP - Add $99 per treatment</li></ul></div>
    <div class="promo" style="top:204px"><span class="promo-dot"></span><h3>TOX &amp; FILLER HAPPY HOUR</h3><ul><li>20 units&nbsp; - $160</li><li>40 units&nbsp; - $320</li><li>Lip Filler - $399*</li><li>Cheek Filler - $490*</li><li>tax not included</li></ul></div>
    <div class="promo" style="top:262px"><span class="promo-dot"></span><h3>CHEMICAL PEELS &amp; MORE</h3><ul><li>Pure Peel + KIT - $109</li><li>Vita Renew Peel + Kit - $160</li><li>OxyLift + Retinol - $109</li></ul></div>
    <div class="promo" style="top:301px"><span class="promo-dot"></span><h3>RESURFACING LASER</h3><ul><li>Single treatment - $600</li></ul></div>
    <div class="promo" style="top:324px"><span class="promo-dot"></span><h3>TATTOO REMOVAL</h3><ul><li>6 Sessions on small area - $534</li></ul></div>

    <div class="photo" style="left:433px;top:93px;width:126px;height:64px;background:linear-gradient(135deg,#2a2a2e 0%,#c99b7f 55%,#e6c3a8 100%)" role="img" aria-label="Gloved hands giving an injection near the eye"></div>
    <div class="photo" style="left:455px;top:161px;width:104px;height:108px;background:linear-gradient(160deg,#e9eef2 0%,#b46b7a 35%,#262324 80%)" role="img" aria-label="Staff member in a face mask holding a product"></div>
    <div class="photo" style="left:427px;top:273px;width:132px;height:77px;background:linear-gradient(135deg,#b8d2dd 0%,#d8b7a0 50%,#8b2e3a 100%)" role="img" aria-label="Laser treatment on a client's back"></div>
  </section>
  <div class="board-label" style="left:817px; top:385px;">Pages 1 &amp; 2 spread</div>

  <!-- Pages 3 & 4 -->
  <section class="spread spread-feature">
    <div class="photo" style="left:0;top:0;width:382px;height:196px;background:linear-gradient(120deg,#eeeeee 0%,#dcdcdc 35%,#e7cdb8 65%,#f1f1f1 100%)" role="img" aria-label="At-home laser hair removal device used on legs resting on white sheets"></div>
    <div class="abs feature-title">
      <span class="ft-is">IS</span>
      <span class="ft-mid">AT-HOME LASER</span>
      <span class="ft-mid">HAIR REMOVAL</span>
      <span class="ft-last">EFFECTIVE?</span>
    </div>
    <div class="photo" style="left:382px;top:0;width:177px;height:190px;background:linear-gradient(150deg,#a9d3df 0%,#d9c7b6 40%,#e7d0be 70%,#9a7b6c 100%)" role="img" aria-label="Gloved technician using a laser handpiece on a client's leg"></div>
    <div class="photo" style="left:280px;top:197px;width:132px;height:164px;background:linear-gradient(160deg,#f0ece8 0%,#e3b79a 45%,#c98a66 75%,#f4f1ee 100%)" role="img" aria-label="Smiling woman in a towel holding a hair removal device under her arm"></div>

    <div class="col" style="left:12px;top:205px">
      <h4>Is At-home Laser Hair Removal Effective?</h4>
      <p class="dropcap-rule">I love how prickly your skin feels. said no one ever! Did you know that the average modern woman shaves 7,718 times in one lifetime? That's a whole lot of bristling, ingrown hairs, and skin irritation. Thankfully laser treatments have rendered razors obsolete. If you're already a firm laser believer, the marketability of handy at-home DIY products can be appealing. But many are left perplexed at their effectiveness. Here are some unbiased professional opinions to zap away your FAQs.</p>
      <h4 class="next">How does laser hair removal work?</h4>
      <p>Laser hair removal uses a concentrated beam of light to target melanin, also known as your natural pigment. Through this, the follicle that produces hair is damaged. This delays the future growth of hairs.</p>
    </div>

    <div class="col" style="left:144px;top:205px">
      <h4>Do at-home laser hair removal gadgets work?</h4>
      <p>NYC's dermatology professionals answer the million-dollar question with a very cautionary yes. Dr. Naveen Darrow claims that results vary according to individuals. Success is dependant on the contrast between your hair and skin color. Light skin and dark hair produce the best outcomes, while other combinations can prove them ineffective. Generally, at-home products are more suitable for use on smaller areas such as your lip and underarms. They can also be beneficial for maintenance after in-office treatments.</p>
      <h4 class="next">Are there any risks involved?</h4>
      <p>There is a risk of hyperpigmentation and skin damage if the device is used inappropriately. Although so, Lumen Medspa esthetician, Jodie Hale claims that FDA approved home devices are generally safe. She said that they are however not as effective as in-office treatments. It is important to thoroughly understand the product before using it. For example, most products are not suitable for breastfeeding or pregnant mothers.</p>
    </div>

    <div class="col" style="left:419px;top:197px;width:130px">
      <h4>Is there a difference in the effectiveness of at-home versus inoffice hair removal treatment?</h4>
      <p>The consensus across the board of professionals is a resounding yes! Laser hair removal is an extremely targeted treatment. It requires calibrated settings that account for both your hair and skin color. Because of safety concerns, most DIY gadgets use Intense Pulse Light (IPL) which is comparatively underpowered and not as effective as a visit to a specialist. Furthermore, with IPL, the less contrast you have between your hair and skin pigment, the higher the risk of skin damage. If you're melanin-blessed, it's best to stay away from at-home devices and seek professional treatment. The difference being, they know what are doing, and can treat all skin tones!</p>
      <h4 class="next">A last word of advice?</h4>
      <p>No matter which you choose, it's important to avoid, tweezing hairs, tanning lotions, antibiotics, and retinoids two weeks prior and post-treatment. Life is too short for anyone to be at war with hair woes. If you don't use it, just lose it!</p>
    </div>
  </section>
  <div class="board-label" style="left:817px; top:801px;">Pages 3 &amp; 4 spread</div>

</body>
</html>
```